PowerPoint Template Design Project

Development of a custom PowerPoint template that is visually attractive.

Target Market(s)

Healthcare Executives

Requirements
Must have
• The template should complement our existing logo, although if the logo is seen as a problem, alternative designs will be considered. The template should provide a title page, table of contents page, header page, and end/back cover page. A recommended color palette should also be defined.

We would prefer that the body of the pages be white, with a watermark graphic (maybe a geometric pattern) that is very faded and fades to white. The watermark should not consume the slide and be limited to only a small amount of the slides printable areas.

The header background should also be a graphically rich element that works well with our existing logo.

The footer should be somewhat pronounced and give some weight to the slide without being overwhelming.

Using our logo's color and/or incorporating additional colors will be important to establishing a cohesive and professional look.
Should not have
• Colored gradients for backgrounds.
Serif Fonts
Text boxes with gradients

```html
<!DOCTYPE html>
<html lang="en">
<head>
<meta charset="utf-8">
<title>Presentation Title</title>
<link rel="stylesheet" href="https://fonts.googleapis.com/css2?family=Open+Sans:wght@700&family=Carlito:wght@400;700&display=swap">
<style>
  :root {
    --navy-deep: #17355e;
    --blue-band: #37639a;
    --panel-light: #dce6f2;
    --canvas-bg: #f2f2f2;
    --grey-disc: #d9d9d9;
    --grey-soft: #e4e4e4;
    --title-navy: #1f3864;
    --subtitle-brown: #984807;
    --brand-orange: #e8572a;
    --brand-grey: #595959;
    --mark-faint: #c8c8c8;
    --white: #ffffff;
  }
  * { margin: 0; padding: 0; box-sizing: border-box; }
  html, body { width: 1200px; height: 900px; overflow: hidden; background: var(--canvas-bg); }
  .slide { position: relative; width: 1200px; height: 900px; overflow: hidden; background: var(--canvas-bg); }
  .slide-shapes { position: absolute; inset: 0; }
  .title-block { position: absolute; left: 0; top: 0; width: 1200px; height: 900px; }
  .slide-title {
    position: absolute; left: 294px; top: 344px;
    font-family: "Open Sans", Arial, sans-serif; font-weight: 700;
    font-size: 70px; line-height: 1; color: var(--title-navy); letter-spacing: 0.5px;
    white-space: nowrap;
  }
  .slide-subtitle {
    position: absolute; left: 565px; top: 455px;
    font-family: "Carlito", Calibri, sans-serif; font-weight: 700;
    font-size: 35px; line-height: 1; color: var(--subtitle-brown);
    white-space: nowrap;
  }
  .brand-badge {
    position: absolute; left: 960px; top: 78px;
    display: flex; align-items: center; gap: 12px;
  }
  .brand-dot { width: 50px; height: 50px; border-radius: 50%; background: var(--brand-orange); flex: none; }
  .brand-name {
    font-family: "Carlito", Calibri, sans-serif; font-weight: 400;
    font-size: 24px; line-height: 1.05; color: var(--brand-grey); text-transform: uppercase;
  }
  .footer-mark {
    position: absolute; left: 35px; top: 788px;
    display: flex; align-items: center; gap: 14px;
  }
  .footer-dot { width: 56px; height: 56px; border-radius: 50%; background: var(--mark-faint); flex: none; }
  .footer-name {
    font-family: "Carlito", Calibri, sans-serif; font-weight: 400;
    font-size: 24px; line-height: 1.05; color: var(--mark-faint); text-transform: uppercase;
  }
</style>
</head>
<body>
<main class="slide">
  <svg class="slide-shapes" width="1200" height="900" viewBox="0 0 1200 900" aria-hidden="true">
    <rect class="header-band-deep" x="0" y="0" width="1200" height="25" fill="var(--navy-deep)"/>
    <rect class="header-band" x="0" y="25" width="1200" height="33" fill="var(--blue-band)"/>
    <circle class="corner-disc-top" cx="45" cy="28" r="182" fill="var(--grey-disc)"/>
    <ellipse class="brand-oval" cx="1085" cy="105" rx="135" ry="68" fill="var(--white)"/>
    <rect class="panel-backing" x="425" y="335" width="830" height="365" rx="40" fill="var(--blue-band)"/>
    <rect class="title-panel" x="315" y="259" width="857" height="412" rx="50" fill="var(--panel-light)"/>
    <circle class="watermark-disc" cx="312" cy="394" r="164" fill="var(--white)" opacity="0.6"/>
    <circle class="watermark-disc-core" cx="312" cy="394" r="154" fill="var(--grey-soft)"/>
    <circle class="corner-disc-bottom" cx="1170" cy="715" r="148" fill="var(--grey-disc)"/>
    <rect class="footer-band" x="0" y="847" width="1200" height="32" fill="var(--blue-band)"/>
    <rect class="footer-band-deep" x="0" y="879" width="1200" height="21" fill="var(--navy-deep)"/>
  </svg>

  <div class="brand-badge">
    <span class="brand-dot"></span>
    <span class="brand-name">Beacon<br>Advisors</span>
  </div>

  <div class="title-block">
    <h1 class="slide-title">Presentation Title</h1>
    <p class="slide-subtitle">Presentation Sub Title</p>
  </div>

  <div class="footer-mark">
    <span class="footer-dot"></span>
    <span class="footer-name">Beacon<br>Advisors</span>
  </div>
</main>
</body>
</html>
```